" Organiza residencias otimizando os espaços, categorizando itens. Com essas soluçoes de organização o cliente encontrara mais tempo disponivel, praticidade e bem estar no seu lar.Organização e transformaçao de vida. "

```html
<!DOCTYPE html>
<html lang="pt">
<head>
<meta charset="utf-8">
<title>Renova – Cartão de visita</title>
<link href="https://fonts.googleapis.com/css2?family=Montserrat:wght@500;600&family=Open+Sans:wght@400;600&display=swap" rel="stylesheet">
<style>
  :root {
    --page: #e9eae6;
    --front-light: #d3ebaa;
    --front-deep: #b7db7c;
    --back-light: #f3f4df;
    --back-deep: #e3e9bf;
    --brand: #7a9232;
    --brand-soft: #9bb04a;
    --olive: #8c8d3a;
    --ink: #4a4b36;
    --muted: #6e6f5e;
    --mark: rgba(150, 170, 70, 0.35);
  }
  * { margin: 0; padding: 0; box-sizing: border-box; }
  html, body { width: 1200px; height: 1200px; overflow: hidden; }
  body {
    background: var(--page);
    position: relative;
    font-family: "Open Sans", Arial, sans-serif;
  }
  .card {
    position: absolute;
    left: 156px;
    width: 895px;
    border-radius: 48px;
    overflow: hidden;
    box-shadow: 0 6px 18px rgba(0,0,0,0.18);
  }
  .card--front {
    top: 67px;
    height: 516px;
    background: radial-gradient(ellipse at 45% 45%, var(--front-light), var(--front-deep));
  }
  .card--back {
    top: 631px;
    height: 509px;
    background: radial-gradient(ellipse at 35% 45%, var(--back-light), var(--back-deep));
  }
  .brand-name {
    font-family: "Montserrat", Arial, sans-serif;
    font-weight: 600;
    color: var(--brand);
    letter-spacing: 1px;
    line-height: 1;
  }
  .brand-tagline {
    font-family: "Montserrat", Arial, sans-serif;
    font-weight: 500;
    color: var(--olive);
    letter-spacing: 1.5px;
    text-transform: uppercase;
  }
  /* front */
  .front-logo {
    position: absolute;
    left: 250px;
    top: 200px;
    display: flex;
    align-items: center;
    gap: 22px;
  }
  .front-logo .mark {
    width: 74px; height: 74px;
    border-radius: 50%;
    background: var(--brand-soft);
  }
  .front-logo .brand-name { font-size: 56px; }
  .front-logo .brand-tagline { font-size: 19px; margin-top: 8px; }
  .front-logo .brand-by {
    font-size: 19px;
    color: var(--olive);
    margin-top: 6px;
    text-align: center;
  }
  /* back */
  .back-mark {
    position: absolute;
    left: 110px;
    top: 90px;
    width: 320px; height: 320px;
    border-radius: 50%;
    background: var(--mark);
  }
  .back-info {
    position: absolute;
    right: 90px;
    top: 48px;
    text-align: right;
  }
  .back-info .brand-name { font-size: 50px; }
  .back-info .brand-tagline { font-size: 18px; margin-top: 6px; }
  .person-name {
    margin-top: 26px;
    font-size: 26px;
    font-weight: 600;
    color: var(--brand);
  }
  .person-role {
    font-size: 22px;
    color: var(--muted);
    letter-spacing: 0.5px;
  }
  .contact-list {
    list-style: none;
    margin-top: 38px;
  }
  .contact-list li {
    display: flex;
    justify-content: flex-end;
    align-items: center;
    gap: 12px;
    font-size: 23px;
    font-weight: 600;
    color: var(--ink);
    height: 54px;
  }
  .contact-icon {
    width: 24px; height: 24px;
    flex: none;
  }
  .contact-square {
    width: 22px; height: 22px;
    border-radius: 4px;
    background: var(--muted);
    flex: none;
  }
</style>
</head>
<body>
  <section class="card card--front">
    <div class="front-logo">
      <span class="mark" aria-hidden="true"></span>
      <div class="brand-block">
        <div class="brand-name">RENOVA</div>
        <div class="brand-tagline">Soluções em organização</div>
        <div class="brand-by">by Helena Duarte</div>
      </div>
    </div>
  </section>

  <section class="card card--back">
    <div class="back-mark" role="img" aria-label="Marca da Renova em destaque"></div>
    <div class="back-info">
      <div class="brand-name">RENOVA</div>
      <div class="brand-tagline">Soluções em organização</div>
      <div class="person-name">Helena Duarte</div>
      <div class="person-role">Personal Organizer</div>
      <ul class="contact-list">
        <li>21 90000 4821
          <svg class="contact-icon" viewBox="0 0 24 24" aria-hidden="true">
            <rect x="5" y="1" width="14" height="22" rx="3" fill="var(--muted)"/>
            <rect x="7.5" y="4" width="9" height="13" fill="#f3f4df"/>
            <circle cx="12" cy="20" r="1.3" fill="#f3f4df"/>
          </svg>
        </li>
        <li>renovaorganiza@mail.com
          <svg class="contact-icon" viewBox="0 0 24 24" aria-hidden="true">
            <rect x="1" y="4" width="22" height="16" rx="2" fill="var(--muted)"/>
            <path d="M2 6 L12 13 L22 6" fill="none" stroke="#f3f4df" stroke-width="2"/>
          </svg>
        </li>
        <li>renovaorganiza/ <span class="contact-square" aria-hidden="true"></span></li>
        <li>renovaorganiza/ <span class="contact-square" aria-hidden="true"></span></li>
      </ul>
    </div>
  </section>
</body>
</html>
```